VENTRIX Hardware needs a Flyer Designed

We need a flyer designed for a marketing strategy that is to be launched by VENTRIX. As it is for our hardware division, our logo should go unto the flyer. We are offering to our customers financing on items from $5000 up to $35000. Here are some key words that you may want to include; "building or revovating? you pick the job we've got the financing." The flyer should reflect some sort of home construction and should be very attractive and vibrant. On the flyer it should also state that it's "hassle-free" and; "no down payment", "no collateral", "affordable monthly payments".

Must Haves [en ]: The companies logo. Also it must state the address of the company and contact info which is; 47 Bellweather Lane Penal, Trinidad. Tel: 555-55-VENTRIX. Email must also be listed: info@ventrixholdings.example.

Nice To Haves [en ]: Good quality graphics. something that is captivating and that will hold the attention of our audience.

Should Not Haves [en ]: Should not be too busy.

Industry/Entity Type

Marketing

Requirements
Must have
• The companies logo. Also it must state the address of the company and contact info which is; 47 Bellweather Lane, Trinidad. Tel: 555-55-VENTRIX. Email must also be listed: info@ventrixholdings.example.
Nice to have
• Good quality graphics. something that is captivating and that will hold the attention of our audience.
Should not have
• Should not be too busy.

```html
<!DOCTYPE html>
<html lang="en">
<head>
<meta charset="utf-8">
<title>VENTRIX Hardware – Building or Renovation Flyer</title>
<link href="https://fonts.googleapis.com/css2?family=Montserrat:wght@500;600;700;800&family=Cinzel:wght@400;500&display=swap" rel="stylesheet">
<style>
  :root {
    --navy: #1f2d5c;
    --royal: #2f4ba6;
    --red: #dc1e3f;
    --white: #ffffff;
    --backdrop: #e9e8e5;
    --ink: #1d1d24;
    --photo-warm: #b98a63;
    --photo-brick: #8e5a45;
    --photo-light: #e8ddd0;
  }
  html, body {
    margin: 0;
    width: 1200px;
    height: 1200px;
    overflow: hidden;
    background: var(--backdrop);
  }
  .flyer {
    position: absolute;
    left: 200px;
    top: 50px;
    width: 800px;
    height: 1100px;
    background: var(--white);
    overflow: hidden;
    box-shadow: 0 6px 24px rgba(0,0,0,.15);
    font-family: "Montserrat", sans-serif;
  }
  .flyer-shapes { position: absolute; inset: 0; }
  .brand {
    position: absolute;
    left: 48px;
    top: 30px;
  }
  .brand-row { display: flex; align-items: center; gap: 10px; }
  .brand-dot {
    flex: none;
    width: 24px; height: 24px; border-radius: 50%;
    background: var(--red);
  }
  .brand-name {
    font-weight: 800;
    font-size: 44px;
    letter-spacing: 1px;
    color: var(--navy);
    line-height: 1;
  }
  .brand-company {
    margin-top: 4px;
    font-size: 9px;
    font-weight: 600;
    color: var(--navy);
    text-align: right;
    border-bottom: 2px solid var(--navy);
    padding-bottom: 3px;
  }
  .brand-group {
    font-size: 10px;
    font-weight: 500;
    color: var(--navy);
    text-align: center;
    letter-spacing: .5px;
    margin-top: 2px;
  }
  .headline {
    position: absolute;
    left: 55px;
    top: 375px;
    margin: 0;
    font-weight: 600;
    color: var(--white);
    line-height: 1;
  }
  .headline span { display: block; }
  .headline-main { font-size: 56px; letter-spacing: 1px; }
  .headline-or { font-size: 42px; color: var(--red); margin: 14px 0 22px; }
  .tagline {
    position: absolute;
    left: 66px;
    top: 590px;
    margin: 0;
    color: var(--white);
    font-weight: 600;
    font-size: 16px;
    font-variant: small-caps;
    line-height: 1.7;
  }
  .tagline em {
    font-style: normal;
    font-variant: normal;
    text-transform: uppercase;
    color: var(--red);
    font-size: 19px;
    letter-spacing: 1px;
  }
  .benefits {
    position: absolute;
    left: 440px;
    top: 555px;
    width: 340px;
    margin: 0;
    padding: 0;
    list-style: none;
    text-align: center;
    color: var(--white);
  }
  .benefit { margin-bottom: 16px; }
  .benefit-icon { display: block; margin: 0 auto 8px; }
  .benefit-label {
    font-weight: 700;
    font-size: 20px;
    letter-spacing: 1px;
    line-height: 1.35;
  }
  .contact {
    position: absolute;
    left: 80px;
    top: 868px;
    width: 340px;
    margin: 0;
    padding: 0;
    list-style: none;
    font-family: "Cinzel", serif;
    font-size: 20px;
    color: var(--ink);
  }
  .contact-item {
    display: flex;
    align-items: flex-start;
    gap: 8px;
    margin-bottom: 18px;
    line-height: 1.25;
  }
  .contact-item svg { flex: none; margin-top: 3px; }
  .contact-email { font-size: 15px; }
</style>
</head>
<body>
<main class="flyer">
  <svg class="flyer-shapes" viewBox="0 0 800 1100" width="800" height="1100">
    <defs>
      <linearGradient id="photoTone" x1="0" y1="0" x2="1" y2="0.6">
        <stop offset="0" stop-color="#ffffff"/>
        <stop offset="0.25" stop-color="#e8ddd0"/>
        <stop offset="0.55" stop-color="#b98a63"/>
        <stop offset="1" stop-color="#8e5a45"/>
      </linearGradient>
    </defs>
    <polygon class="photo-area" role="img" aria-label="Photo of a builder in a hard hat and a smiling couple reviewing house plans in front of a brick home"
             points="200,0 800,0 800,500 660,470 0,160 0,120" fill="url(#photoTone)"/>
    <polygon class="panel-red" points="355,690 700,470 800,480 800,1100 475,1100" fill="var(--red)"/>
    <polygon class="band-royal" points="0,160 675,470 0,885" fill="var(--royal)"/>
    <polygon class="panel-navy" points="0,185 635,472 0,860" fill="var(--navy)"/>
  </svg>

  <div class="brand">
    <div class="brand-row">
      <span class="brand-name">VENTRIX</span>
      <span class="brand-dot"></span>
    </div>
    <div class="brand-company">Ventrix Trading Company Limited</div>
    <div class="brand-group">GROUP OF COMPANIES</div>
  </div>

  <h1 class="headline">
    <span class="headline-main">BUILDING</span>
    <span class="headline-or">OR</span>
    <span class="headline-main">RENOVATION</span>
  </h1>

  <p class="tagline">
    You pick the &ldquo;<em>Job</em>&rdquo;<br>
    We've got the &ldquo;<em>Financing</em>&rdquo;
  </p>

  <ul class="benefits">
    <li class="benefit">
      <svg class="benefit-icon" width="40" height="40" viewBox="0 0 40 40">
        <circle cx="20" cy="20" r="19" fill="var(--white)"/>
        <path d="M12 19h5v11h-5z M18 19l4-8c2 0 3 1 3 3l-1 4h5c1.5 0 2.5 1.5 2 3l-2 7c-.4 1.3-1.4 2-2.6 2H18z" fill="var(--red)"/>
      </svg>
      <span class="benefit-label">HASSLE - FREE</span>
    </li>
    <li class="benefit">
      <svg class="benefit-icon" width="30" height="50" viewBox="0 0 30 50">
        <rect x="7" y="2" width="16" height="3" fill="var(--white)"/>
        <rect x="7" y="8" width="16" height="3" fill="var(--white)"/>
        <path d="M7 14h16v16h6L15 48 1 30h6z" fill="var(--white)"/>
        <text x="15" y="28" font-size="11" font-weight="700" text-anchor="middle" fill="var(--red)" font-family="Montserrat, sans-serif">$</text>
      </svg>
      <span class="benefit-label">NO DOWN PAYMENT</span>
    </li>
    <li class="benefit">
      <svg class="benefit-icon" width="46" height="46" viewBox="0 0 46 46">
        <circle cx="23" cy="23" r="21" fill="none" stroke="var(--white)" stroke-width="3"/>
        <rect x="14" y="11" width="16" height="21" fill="none" stroke="var(--white)" stroke-width="2.5"/>
        <path d="M17 17h10M17 22h10M17 27h5" stroke="var(--white)" stroke-width="2"/>
        <path d="M24 30l4 4 8-9" fill="none" stroke="var(--white)" stroke-width="3"/>
      </svg>
      <span class="benefit-label">NO COLLATERAL</span>
    </li>
    <li class="benefit">
      <svg class="benefit-icon" width="56" height="46" viewBox="0 0 56 46">
        <rect x="4" y="16" width="30" height="16" fill="var(--white)"/>
        <rect x="8" y="28" width="30" height="16" fill="var(--white)" stroke="var(--red)" stroke-width="2"/>
        <circle cx="23" cy="36" r="4" fill="var(--red)"/>
        <path d="M30 18c6-2 10-8 18-14l5 6c-6 5-10 12-18 14z" fill="var(--white)"/>
      </svg>
      <span class="benefit-label">AFFORDABLE<br>MONTHLY PAYMENTS</span>
    </li>
  </ul>

  <ul class="contact">
    <li class="contact-item">
      <svg width="18" height="24" viewBox="0 0 18 24">
        <path d="M9 1C4.6 1 1.5 4.2 1.5 8.3 1.5 14 9 21 9 21s7.5-7 7.5-12.7C16.5 4.2 13.4 1 9 1z" fill="none" stroke="var(--ink)" stroke-width="2"/>
        <circle cx="9" cy="8.5" r="2.6" fill="var(--ink)"/>
        <path d="M2 23h14" stroke="var(--ink)" stroke-width="2"/>
      </svg>
      <span>47, Bellweather Lane, Marlow Bay, Corvania</span>
    </li>
    <li class="contact-item">
      <svg width="20" height="20" viewBox="0 0 20 20">
        <circle cx="10" cy="10" r="9" fill="none" stroke="var(--ink)" stroke-width="1.6"/>
        <path d="M7 5l2 3-1.3 1.3c.7 1.4 1.7 2.4 3 3L12 11l3 2-1 2c-4 0-8-4-8-8z" fill="var(--ink)"/>
      </svg>
      <span>555 - 55 &nbsp;VENTRIX</span>
    </li>
    <li class="contact-item">
      <svg width="20" height="20" viewBox="0 0 20 20">
        <circle cx="10" cy="10" r="9.5" fill="var(--ink)"/>
        <rect x="4.5" y="6" width="11" height="8" fill="none" stroke="var(--white)" stroke-width="1.4"/>
        <path d="M4.5 6l5.5 4.5L15.5 6M4.5 14l4-4M15.5 14l-4-4" fill="none" stroke="var(--white)" stroke-width="1.2"/>
      </svg>
      <span class="contact-email">info@ventrixholdings.example</span>
    </li>
  </ul>
</main>
</body>
</html>
```